New Letterhead request for our Law Firm!

We are a small Estate Planning Firm who just got out logo redesigned. It's attached. We need some letterhead for our client welcome letters and so forth. Clean, bright, and approachable is our style. If you need the specifications for our color scheme or other versions of the logo file, we have those too. Visit our website to get an idea about our services/aesthetics:https://willowmere.law/

Target Market(s)

Adults 30-80

Colors

Designer to choose colors to be used in the design.

Requirements
Must have
• Logo with color. Contact information

```html
<!DOCTYPE html>
<html lang="en">
<head>
<meta charset="utf-8">
<title>Willowmere Law Firm Letterhead</title>
<link rel="stylesheet" href="https://fonts.googleapis.com/css2?family=Lato:wght@400;700&display=swap">
<style>
  :root {
    --backdrop: #cfc6c3;
    --paper: #fdfdfb;
    --sage: #6e9e8c;
    --sage-faint: #eef2f0;
    --slate: #4a4b50;
    --ink: #3b3c40;
  }
  * { margin: 0; padding: 0; box-sizing: border-box; }
  html, body {
    width: 1200px; height: 784px; overflow: hidden;
    background: var(--backdrop);
    font-family: "Lato", Arial, sans-serif;
  }
  .letterhead {
    position: absolute; left: 322px; top: 32px;
    width: 556px; height: 720px;
    background: var(--paper);
    box-shadow: 0 6px 18px rgba(0,0,0,.12);
    overflow: hidden;
  }
  .band-sage {
    position: absolute; left: 0; top: 0;
    width: 338px; height: 20px; background: var(--sage);
  }
  .band-slate {
    position: absolute; left: 346px; top: 0;
    right: 0; height: 20px; background: var(--slate);
  }
  .brand {
    position: absolute; right: 34px; top: 36px;
    display: flex; align-items: center; gap: 10px;
  }
  .brand-circle {
    width: 38px; height: 38px; border-radius: 50%;
    border: 2px solid var(--sage);
  }
  .brand-name {
    font-weight: 700; font-size: 18px; color: var(--sage);
    letter-spacing: .5px;
  }
  .backdrop-mark {
    position: absolute; left: 168px; top: 250px;
    width: 250px; height: 250px; border-radius: 50%;
    background: var(--sage-faint);
  }
  .contact {
    position: absolute; left: 26px; top: 20px;
    display: flex; gap: 10px;
  }
  .contact-icons {
    width: 22px; padding: 8px 0 6px;
    border: 1.5px solid var(--sage); border-top: none;
    border-radius: 0 0 4px 4px;
    display: flex; flex-direction: column; align-items: center; gap: 7px;
  }
  .contact-icons svg { width: 11px; height: 11px; fill: var(--sage); }
  .contact-lines {
    padding-top: 8px; font-size: 9.5px; line-height: 14px; color: var(--ink);
  }
  .contact-firm { color: var(--sage); font-weight: 700; }
</style>
</head>
<body>
  <main class="letterhead">
    <div class="band-sage"></div>
    <div class="band-slate"></div>

    <div class="brand">
      <div class="brand-circle"></div>
      <span class="brand-name">Willowmere Law Firm</span>
    </div>

    <div class="backdrop-mark" aria-hidden="true"></div>

    <address class="contact" style="font-style:normal">
      <div class="contact-icons">
        <svg viewBox="0 0 12 12" aria-label="Address"><path d="M6 0a4 4 0 0 0-4 4c0 3 4 8 4 8s4-5 4-8a4 4 0 0 0-4-4zm0 5.6A1.6 1.6 0 1 1 6 2.4a1.6 1.6 0 0 1 0 3.2z"/></svg>
        <svg viewBox="0 0 12 12" aria-label="Phone"><path d="M2.4 0.6l1.8 2.4-1 1.2c.6 1.4 1.8 2.6 3.2 3.2l1.2-1 2.4 1.8-1 2.2C4.6 10.2 1.8 7.4 0.2 3l2.2-2.4z"/></svg>
        <svg viewBox="0 0 12 12" aria-label="Email"><path d="M0 2h12v8H0zM1.2 3v.3L6 6.6l4.8-3.3V3L6 6.1z"/></svg>
        <svg viewBox="0 0 12 12" aria-label="Website"><path d="M6 0a6 6 0 1 0 0 12A6 6 0 0 0 6 0zm0 1.2c.8.8 1.3 2.4 1.4 4.2H4.6C4.7 3.6 5.2 2 6 1.2zM1.3 6.6h2.1c.1 1.6.5 3 1.1 3.9a4.8 4.8 0 0 1-3.2-3.9zm0-1.2a4.8 4.8 0 0 1 3.2-3.9c-.6.9-1 2.3-1.1 3.9zm4.7 5.4c-.8-.8-1.3-2.4-1.4-4.2h2.8c-.1 1.8-.6 3.4-1.4 4.2zm1.5-.3c.6-.9 1-2.3 1.1-3.9h2.1a4.8 4.8 0 0 1-3.2 3.9zm1.1-5.1c-.1-1.6-.5-3-1.1-3.9a4.8 4.8 0 0 1 3.2 3.9z"/></svg>
      </div>
      <div class="contact-lines">
        <div class="contact-firm">Willowmere Law Firm, PLLC</div>
        <div>2450 Lakeview Parkway, Suite 310</div>
        <div>Maple Grove, MN 55369</div>
        <div>612-555-0147</div>
        <div>info@willowmere.law</div>
        <div>www.willowmere.law</div>
      </div>
    </address>
  </main>
</body>
</html>
```